Name should be The MORVANE. Please use logo and number 555 284 3170. Also should state "NOW LEASING".
Colors:
Witching hour (2120-30) HEX color #46494F
White Dove (OC-17) HEX color: #EFEEE5
Wilmington Tan (HC-34) HEX color: #CCB084
Oxford Gray (2128-40) HEX Color: #8290A0
Black

Target Market(s)

Renters

Industry/Entity Type

luxury rentals

Font styles to use
Serif

Colors
0054AA
0677BA
7BADD7
CADEEF
E8F1F8

Requirements
Must have
• Solid Colors and leasing information
Nice to have
• modern design, pattern
Should not have
• bright colors, bold text,

```html
<!DOCTYPE html>
<html lang="en">
<head>
<meta charset="utf-8">
<title>The Morvane — Now Leasing Banner</title>
<link rel="stylesheet" href="https://fonts.googleapis.com/css2?family=Cinzel:wght@400&family=EB+Garamond:wght@400&display=swap">
<style>
  :root {
    --slate: #4a4e54;
    --tan: #ceae7f;
    --white: #ffffff;
    --ink: #020304;
    --page: #fdfdfd;
  }
  html, body {
    margin: 0;
    padding: 0;
    width: 876px;
    height: 1200px;
    overflow: hidden;
    background: var(--page);
  }
  .canvas {
    position: relative;
    width: 876px;
    height: 1200px;
  }
  .banner {
    position: absolute;
    left: 0;
    top: 0;
  }
  .brand-name {
    font-family: "Cinzel", serif;
    fill: var(--white);
  }
  .brand-sub {
    font-family: "Cinzel", serif;
    fill: var(--tan);
  }
  .property-name {
    font-family: "Cinzel", serif;
    fill: var(--white);
  }
  .phone {
    font-family: "EB Garamond", serif;
    font-variant-numeric: oldstyle-nums;
    fill: var(--tan);
  }
  .rule { stroke: var(--tan); stroke-width: 4; }
  .leasing-now {
    font-family: "Cinzel", serif;
    fill: var(--tan);
  }
  .leasing-word {
    font-family: "Cinzel", serif;
    fill: var(--white);
  }
</style>
</head>
<body>
<div class="canvas">
  <svg class="banner" width="876" height="1200" viewBox="0 0 876 1200" xmlns="http://www.w3.org/2000/svg">
    <!-- main panel -->
    <polygon points="303,104 573,104 573,947 303,923" fill="var(--slate)"/>
    <!-- edge strip -->
    <rect x="303" y="104" width="21" height="819" fill="var(--tan)" role="img" aria-label="Tan zigzag edge pattern"/>
    <!-- tan sash -->
    <polygon points="303,922 573,946 573,954 303,930" fill="var(--tan)"/>
    <!-- black footer -->
    <polygon points="303,939 573,961 573,1125 303,1125" fill="var(--ink)"/>

    <!-- brand -->
    <text class="brand-name" x="437" y="222" text-anchor="middle" font-size="52" textLength="173" lengthAdjust="spacingAndGlyphs">BRENTON</text>
    <text class="brand-sub" x="437" y="245" text-anchor="middle" font-size="14" letter-spacing="6" textLength="176" lengthAdjust="spacing">PROPERTIES</text>

    <!-- property name, vertical -->
    <text class="property-name" transform="translate(440 584) rotate(-90)" text-anchor="middle" font-size="94" textLength="614" lengthAdjust="spacingAndGlyphs">THE MORVANE</text>

    <!-- phone, vertical -->
    <line class="rule" x1="492" y1="278" x2="492" y2="353"/>
    <text class="phone" transform="translate(518 580) rotate(-90)" text-anchor="middle" font-size="68" textLength="406" lengthAdjust="spacingAndGlyphs">555.284.3170</text>
    <line class="rule" x1="492" y1="807" x2="492" y2="886"/>

    <!-- leasing -->
    <text class="leasing-now" x="446" y="1017" text-anchor="middle" font-size="56" textLength="138" lengthAdjust="spacingAndGlyphs">NOW</text>
    <text class="leasing-word" x="440" y="1067" text-anchor="middle" font-size="58" textLength="210" lengthAdjust="spacingAndGlyphs">LEASING</text>
  </svg>
</div>
</body>
</html>
```